Website Landing Page for Marlowe Systems

Create a custom designed website landing page for our business. Looking for a professional upscale design that incorporates our logo and logo colors into the theme. I want a standard fixed frame website, not a constant scrolling format that seems to be the trend. To start with I'm looking for more of the graphic design part, maybe a concept or theme, I don't expect to see a finished project. Not interested in generic templates or layouts.

The name of our company is Marlowe Systems and I've attached our logo below. I'd like to have the web page have the same look and feel of our logo, as well as the colors. Our company, Marlowe Systems does system design, installation, and programming, of residential and commercial Audio/Video and Automation systems. We do home theaters, lighting and building automation, video conferencing systems, security camera installations, conference rooms, projectors, distributed audio systems, and similar Technology projects. This will be a professional services/informational website. We will not sell products on this website. This website will be used to advertise our company and communicate our services to prospective customers. Having a well designed, professional and clean website is one way we want to distinguish our company from the competition.

Here are some examples of what I consider a professional well designed website
http://www.qrzstudio.example/Work/

Last year we had our tradeloft store designed (with PixelHarbor) and I'm really happy with the way it turned out. You can see it at www.KelpGearDepot.example I consider this to be a great design and looking for the same level of quality with this new website. However, do not copy or use any part of this design in this new project. This tradeloft store is completely separate from our other company Marlowe Systems. I only mention this tradeloft store an an example of good work.

Target Market(s)

People interested in Audio/Video, home theaters, home automation. We do sales, system design, and programming. We typically work on larger projects with both residential and commercial customers.

Industry/Entity Type

Business

Number of Pages Required

1 page

Requirements
Must have
• Great design elements. Please use a white background. I think white goes well with our logo colors.

```html
<!DOCTYPE html>
<html lang="en">
<head>
<meta charset="utf-8">
<title>Marlowe Systems</title>
<link rel="stylesheet" href="https://fonts.googleapis.com/css2?family=Source+Sans+3:wght@300;400;600;700&display=swap">
<style>
:root{
  --blue:#2f7fc6;
  --blue-light:#35a8df;
  --blue-deep:#1d5f9e;
  --green:#7cc24e;
  --green-deep:#5cae36;
  --band:#3a9bd5;
  --ink:#5a5a5a;
  --ink-soft:#7a7a7a;
  --footer:#000;
  --footer-text:#bdbdbd;
  --white:#fff;
  --orange:#f29b12;
}
*{box-sizing:border-box;margin:0;padding:0}
html,body{width:914px;height:1200px;overflow:hidden;background:var(--white)}
body{position:relative;font-family:"Source Sans 3",sans-serif;color:var(--ink)}
.abs{position:absolute}

/* header */
.site-header{left:0;top:0;width:914px;height:63px;background:var(--white)}
.brand{left:118px;top:8px;display:flex;align-items:center;gap:9px}
.brand-dot{width:46px;height:46px;border-radius:50%;border:5px solid var(--blue)}
.brand-name{font-weight:600;font-size:14px;line-height:14px;color:var(--blue);letter-spacing:.5px;text-transform:uppercase}
.main-nav{right:123px;top:27px;display:flex;gap:15px;font-size:10.5px;color:var(--ink)}

/* hero */
.hero{left:0;top:63px;width:914px;height:475px;
  background:radial-gradient(ellipse at 50% 45%,#3d8fc9 0%,#2a73b3 55%,#1c5a95 100%)}
.hero-ring{left:312px;top:134px;width:284px;height:284px;border-radius:50%;border:18px solid rgba(255,255,255,.22)}
.hero-title{left:0;top:166px;width:914px;text-align:center;color:var(--white);font-weight:600;font-size:26px;letter-spacing:.2px}
.hero-sub{left:0;top:207px;width:914px;text-align:center;color:var(--white);font-weight:600;font-size:9.6px}
.hero-cta{left:377px;top:240px;width:157px;height:36px;background:var(--green-deep);color:var(--white);
  font-size:11px;display:flex;align-items:center;justify-content:center;letter-spacing:.3px}

/* services grid */
.service{height:52px;display:flex;align-items:center;gap:9px;padding-left:16px;color:var(--white);
  font-weight:600;font-size:9.6px;line-height:11px;text-transform:uppercase;
  background:linear-gradient(180deg,var(--blue-light),var(--blue))}
.service svg{flex:none}
.service.all{background:linear-gradient(180deg,#6cc04a,var(--green-deep))}

/* intro */
.intro-dot{left:438px;top:683px;width:38px;height:38px;border-radius:50%;border:3px solid var(--blue)}
.intro-title{left:0;top:737px;width:914px;text-align:center;color:var(--blue);font-size:18px}
.intro-sub{left:0;top:766px;width:914px;text-align:center;font-weight:600;font-size:9px;color:var(--ink)}
.intro-text{left:140px;top:798px;width:634px;text-align:center;font-weight:300;font-size:8.4px;line-height:14.8px;color:var(--ink-soft)}
.intro-cta{left:390px;top:861px;width:131px;height:28px;background:var(--green);color:var(--white);
  font-weight:600;font-size:9.6px;display:flex;align-items:center;justify-content:center}

/* subscribe */
.offers{left:0;top:944px;width:914px;height:60px;background:var(--band)}
.offers-title{left:120px;top:960px;color:var(--white);font-weight:600;font-size:12.5px}
.offers-sub{left:120px;top:977px;color:var(--white);font-size:9.5px}
.offers-input{left:574px;top:965px;width:186px;height:24px;background:var(--white);border-radius:2px;
  font-size:6.5px;color:#333;padding-left:9px;display:flex;align-items:center}
.offers-go{left:766px;top:965px;width:25px;height:24px;border-radius:2px;background:linear-gradient(180deg,#f7b824,var(--orange));
  color:var(--white);font-weight:700;font-size:8px;display:flex;align-items:center;justify-content:center}

/* footer */
.site-footer{left:0;top:1004px;width:914px;height:196px;background:var(--footer)}
.footer-col{top:1038px;color:var(--footer-text)}
.footer-col h4{font-weight:400;font-size:9.5px;color:#e0e0e0;margin-bottom:10px}
.footer-col li{list-style:none;font-size:7.6px;line-height:17.2px}
.footer-brand{left:584px;top:1062px;display:flex;align-items:center;gap:12px}
.footer-brand-dot{width:70px;height:70px;border-radius:50%;border:6px solid #3a3a3a}
.footer-brand-name{font-weight:600;font-size:20px;line-height:20px;color:#3a3a3a;text-transform:uppercase;letter-spacing:.5px}
.copyright{left:119px;top:1180px;font-size:7.6px;color:#d0d0d0}
.social{right:122px;top:1180px;display:flex;gap:6px;font-size:7px;font-weight:600;color:#e0e0e0}
</style>
</head>
<body>

<header class="site-header abs">
  <div class="brand abs"><span class="brand-dot"></span><span class="brand-name">Marlowe<br>Systems</span></div>
  <nav class="main-nav abs"><span>Home</span><span>About Us</span><span>Services</span><span>Clients</span><span>Support</span><span>Contact Us</span></nav>
</header>

<section class="hero abs" role="img" aria-label="Blue-tinted collage of audio/video equipment: laptop, desk phones, tablet and security camera"></section>
<div class="hero-ring abs"></div>
<h1 class="hero-title abs">WELCOME TO MARLOWE SYSTEMS</h1>
<p class="hero-sub abs">WE DO SYSTEM DESIGN, INSTALLATION, AND PROGRAMMING, OF RESIDENTIAL AND COMMERCIAL AUDIO/VIDEO AND AUTOMATION SYSTEMS</p>
<div class="hero-cta abs">GET STARTED NOW!</div>

<div class="service abs" style="left:120px;top:538px;width:170px">
  <svg width="38" height="24" viewBox="0 0 38 24" fill="#fff"><rect x="0" y="2" width="5" height="20"/><rect x="33" y="2" width="5" height="20"/><rect x="8" y="1" width="22" height="15" fill="none" stroke="#fff" stroke-width="2"/><rect x="12" y="19" width="14" height="3"/></svg>
  <span>Home Theaters</span></div>
<div class="service abs" style="left:292px;top:538px;width:164px">
  <svg width="20" height="28" viewBox="0 0 20 28" fill="#fff"><circle cx="10" cy="9" r="8"/><rect x="6" y="18" width="8" height="6"/><rect x="7" y="25" width="6" height="2"/></svg>
  <span>Lighting &amp; Building<br>Automation</span></div>
<div class="service abs" style="left:458px;top:538px;width:166px">
  <svg width="32" height="26" viewBox="0 0 32 26" fill="#fff"><rect x="1" y="1" width="30" height="19" fill="none" stroke="#fff" stroke-width="2"/><circle cx="10" cy="9" r="3"/><circle cx="22" cy="9" r="3"/><rect x="5" y="13" width="22" height="5"/><rect x="12" y="21" width="8" height="4"/></svg>
  <span>Video Conferencing<br>Systems</span></div>
<div class="service abs" style="left:626px;top:538px;width:163px">
  <svg width="38" height="26" viewBox="0 0 38 26" fill="#fff"><polygon points="8,4 34,12 31,18 6,11"/><rect x="14" y="13" width="3" height="7"/><rect x="1" y="18" width="3" height="8"/><rect x="2" y="20" width="14" height="3"/></svg>
  <span>Security Camera<br>Installations</span></div>

<div class="service abs" style="left:120px;top:591px;width:170px">
  <svg width="32" height="28" viewBox="0 0 32 28" fill="#fff"><circle cx="9" cy="5" r="3"/><circle cx="16" cy="4" r="3"/><circle cx="23" cy="5" r="3"/><rect x="4" y="12" width="24" height="6"/><rect x="2" y="10" width="4" height="16"/><rect x="26" y="10" width="4" height="16"/><rect x="13" y="18" width="6" height="8"/></svg>
  <span>Conference Rooms</span></div>
<div class="service abs" style="left:292px;top:591px;width:164px">
  <svg width="48" height="22" viewBox="0 0 48 22" fill="#fff"><rect x="1" y="2" width="46" height="18" rx="6"/><circle cx="36" cy="11" r="6" fill="#2f7fc6"/><circle cx="36" cy="11" r="3"/><rect x="7" y="7" width="3" height="8" fill="#2f7fc6"/><rect x="12" y="7" width="3" height="8" fill="#2f7fc6"/><rect x="17" y="7" width="3" height="8" fill="#2f7fc6"/></svg>
  <span>Projectors</span></div>
<div class="service abs" style="left:458px;top:591px;width:166px">
  <svg width="32" height="28" viewBox="0 0 32 28" fill="#fff"><rect x="1" y="1" width="30" height="20" fill="none" stroke="#fff" stroke-width="2"/><polygon points="10,9 14,9 19,5 19,17 14,13 10,13"/><rect x="12" y="22" width="8" height="3"/><rect x="8" y="25" width="16" height="2"/></svg>
  <span>Distributed Audio<br>Systems</span></div>
<div class="service all abs" style="left:626px;top:591px;width:163px">
  <svg width="30" height="28" viewBox="0 0 30 28"><circle cx="11" cy="11" r="8" fill="none" stroke="#fff" stroke-width="3.5"/><line x1="17" y1="17" x2="27" y2="25" stroke="#fff" stroke-width="5" stroke-linecap="round"/></svg>
  <span>View All Services</span></div>

<div class="intro-dot abs"></div>
<h2 class="intro-title abs">SYSTEM DESIGN, INSTALLATION, AND PROGRAMMING</h2>
<p class="intro-sub abs">WE DO SYSTEM DESIGN, INSTALLATION, AND PROGRAMMING, OF RESIDENTIAL AND COMMERCIAL AUDIO/VIDEO AND AUTOMATION SYSTEMS</p>
<p class="intro-text abs">Our company, Marlowe Systems does system design, installation, and programming, of residential and commercial Audio/Video and Automation systems.<br>We do home theaters, lighting and building automation, video conferencing systems, security camera installations, conference rooms, projectors,<br>distributed audio systems, and similar Technology projects.</p>
<div class="intro-cta abs">MORE ABOUT US</div>

<section class="offers abs"></section>
<h3 class="offers-title abs">DON’T MISS OUR ATTRACTIVE OFFERS</h3>
<p class="offers-sub abs">Subscribe To Recieve the Latest Offers</p>
<div class="offers-input abs">Enter Your Email Address</div>
<div class="offers-go abs">GO</div>

<footer class="site-footer abs"></footer>
<div class="footer-col abs" style="left:120px"><h4>Quick Links</h4><ul><li>Home</li><li>About Us</li><li>Client</li><li>Support</li><li>Contact Us</li></ul></div>
<div class="footer-col abs" style="left:280px"><h4>Useful Links</h4><ul><li>Link Number 1</li><li>Link Number 2</li><li>Link Number 3</li><li>Link Number 4</li><li>Link Number 5</li></ul></div>
<div class="footer-col abs" style="left:446px"><h4>Services</h4><ul><li>Service Number 1</li><li>Service Number 2</li><li>Service Number 3</li><li>Service Number 4</li><li>Service Number 5</li></ul></div>
<div class="footer-brand abs"><span class="footer-brand-dot"></span><span class="footer-brand-name">Marlowe<br>Systems</span></div>
<p class="copyright abs">© 2017 by, Marlowe Systems. All Rights Reserved.</p>
<div class="social abs"><span>Facetome</span><span>Linkwell</span><span>Chirpa</span><span>Gloop</span></div>

</body>
</html>
```